Speisekarte Heuriger
Zielgruppe
Wir sind ein Gastronomielokal im Burgenland. Ein Heuriger ist ein traditionelles Lokal in dem hauptsächlich kalte und einfache warme Speisen verabreicht werden. (Brote, kaltes und warmes gebratenes Fleisch, gemischte Teller, Strudl usw.) Aber ein großer Schwerpunkt liegt dabei auch immer auf den eigenen Weinen.
Aufgabenstellung
Da ein Heuriger aus dem Weinbau und somit Landwirtschaft kommt bevorzuge ich eher ein schlichtes traditionelles Design. Ein grüner Farbbereich ist vielleicht das Beste. (nicht stechend grün. eher hell) (Vielleicht im Internet nach Speisekarte Heuriger/Buschenschank suchen)
Ich benötige eine Vorlage für die Speisekarte in Indesign am besten erstellt mit dem drukwelle.at plugin damit die Größen passen.
Speisekarte mit Umschlag 8 Innenseiten mit 4seitigem Umschlag haben.
In A5 hoch
CMYK-Farbmodell
Klammerheftung
Umschlag:
Vorderseite natürlich mit "Speisekarte" drauf mit Logo, Und evtl der Name: "Heuriger Familie Pelkinger" usw.
die vordere Innenseite kann leer sein. Evtl auch gesamte Anschrift hier rein. Oder auch auf die Rückseite. Das ist freigestellt.
Auf der hinteren Innenseite muss die Allergenverordnung mit den Allergenen und dazugehörigen Buchstaben vorhanden sein! (Achtung für Österreich! Gibt genug Beispielbilder im Internet)
Auf der Rückseite hinten sollte stehen: "Wir bedanken uns für Ihren Besuch und freuen uns darauf, Sie bald wieder bei uns begrüßen zu dürfen!
Familie Pelkinger" (Natürlich nicht in einer Wurst)
Innenseiten: (Text schreibe ich selber. Aber vielleicht ein paar Beispiele für Schriftart und Größe/Farbe)
Erste Seite (rechts): Getränke
Zweite Seite: Kalte Speisen
Dritte Seite: Brote
Vierte Seite: Warme Speisen
Fünfte Seite: Beilagen/Salate
Sechste Seite: Für unsere kleinen Gäste/ Strudel
Siebente Seite: Weißwein
Achte Seite: Rotwein
Die Seitenbelegung ist nur als Info gedacht. Ich habe leider keine schönen Fotos von den Speisen gemacht und will auch keine fremden Speisen in meiner Karte sehen. Also keine Speisebilder. (Mit Ausnahme von Weintrauben vielleicht. Bezug zum Weinbau usw.)
Anbei habe ich die Logos von unseren Etiketten. Man kann das P auch alleine ohne dem Namen darunt..

```html
<!DOCTYPE html>
<html lang="de">
<head>
<meta charset="utf-8">
<title>Speisekarte – Heuriger Familie Pelkinger</title>
<link href="https://fonts.googleapis.com/css2?family=Jost:wght@400;500;600&display=swap" rel="stylesheet">
<style>
  :root {
    --paper: #f2f2e4;
    --green: #6cbf2a;
    --ink: #1e1e1e;
    --icon-fg: #ffffff;
  }
  * { margin: 0; padding: 0; box-sizing: border-box; }
  html, body { width: 1200px; height: 849px; overflow: hidden; background: var(--paper); }
  body { font-family: "Jost", sans-serif; color: var(--ink); }
  .spread { position: relative; width: 1200px; height: 849px; }
  .page { position: absolute; top: 0; width: 600px; height: 849px; }
  .page--left { left: 0; }
  .page--right { left: 600px; }

  .brand {
    position: absolute; top: 62px; left: 0; width: 100%;
    display: flex; justify-content: center; align-items: center; gap: 10px;
    color: var(--green); font-size: 30px; font-weight: 400; letter-spacing: 1px;
  }
  .brand__square { width: 16px; height: 16px; background: var(--green); }

  .section-head { position: absolute; border-bottom: 1px solid var(--green); height: 30px; }
  .section-head__title {
    position: absolute; bottom: 5px; font-size: 19px; font-weight: 400;
    letter-spacing: 1px; text-transform: uppercase; white-space: nowrap;
  }
  .section-head svg { position: absolute; }

  .menu-item {
    position: absolute; left: 75px; width: 437px;
    display: flex; justify-content: space-between; font-size: 13.5px;
  }
  .menu-item__name { font-weight: 600; }
  .menu-item__note { font-weight: 400; }
  .menu-item__price { font-weight: 600; }

  .footer { position: absolute; top: 744px; width: 216px; text-align: center; }
  .footer__name {
    color: var(--green); font-size: 10.5px; letter-spacing: 0.4px;
    padding-bottom: 4px; border-bottom: 1px solid var(--green); text-transform: uppercase;
  }
  .footer__icons { display: flex; justify-content: center; gap: 13px; margin-top: 12px; }
  .footer__icon { width: 42px; height: 42px; background: var(--green); display: block; }
</style>
</head>
<body>
<main class="spread">

  <!-- Seite: Für unsere kleinen Gäste / Strudel -->
  <section class="page page--left">
    <div class="brand"><span class="brand__square"></span>Pelkinger</div>

    <header class="section-head" style="left:77px; top:173px; width:446px;">
      <svg style="left:6px; top:0;" width="98" height="26" viewBox="0 0 98 26">
        <path d="M2 6 Q40 2 72 4 Q80 5 80 7 Q60 10 2 9 Z" fill="var(--green)"/>
        <rect x="30" y="17" width="48" height="3" rx="1.5" fill="var(--green)"/>
        <path d="M76 15 H96 M76 18.5 H96 M76 22 H96" stroke="var(--green)" stroke-width="1.3"/>
      </svg>
      <h2 class="section-head__title" style="left:118px;">Für unsere kleinen Gäste</h2>
    </header>

    <div class="menu-item" style="top:243px;"><span><span class="menu-item__name">Tigerle |</span> <span class="menu-item__note">(kleines Wurstbrot)</span></span><span class="menu-item__price">€ 1.50</span></div>
    <div class="menu-item" style="top:288px;"><span><span class="menu-item__name">Honigbär |</span> <span class="menu-item__note">(kleiner Wurstsalat)</span></span><span class="menu-item__price">€ 2.50</span></div>
    <div class="menu-item" style="top:334px;"><span><span class="menu-item__name">Spürnase |</span> <span class="menu-item__note">(1 Scheibe Surbraten + Salat)</span></span><span class="menu-item__price">€ 3.00</span></div>

    <header class="section-head" style="left:142px; top:414px; width:325px;">
      <svg style="left:77px; top:10px;" width="76" height="12" viewBox="0 0 76 12">
        <rect x="0" y="4.5" width="50" height="3" rx="1.5" fill="var(--green)"/>
        <path d="M50 6 L56 6 M56 2 H74 M56 6 H74 M56 10 H74" stroke="var(--green)" stroke-width="1.4"/>
      </svg>
      <h2 class="section-head__title" style="left:158px;">Strudel</h2>
    </header>

    <div class="menu-item" style="top:496px;"><span class="menu-item__name">Apfelstrudel</span><span class="menu-item__price">€ 3.00</span></div>
    <div class="menu-item" style="top:540px;"><span class="menu-item__name">Topfenstrudel</span><span class="menu-item__price">€ 3.50</span></div>
    <div class="menu-item" style="top:587px;"><span class="menu-item__name">Bohnenstrudel</span><span class="menu-item__price">€ 3.00</span></div>
    <div class="menu-item" style="top:631px;"><span class="menu-item__name">Vanillesauce</span><span class="menu-item__price">€ 0.50</span></div>

    <footer class="footer" style="left:186px;">
      <p class="footer__name">Heuriger Familie Pelkinger e.U.</p>
      <div class="footer__icons">
        <svg class="footer__icon" viewBox="0 0 42 42"><path d="M13 8 H29 Q30 22 21 24 Q12 22 13 8 Z M20 24 V34 M15 34 H27" fill="var(--icon-fg)" stroke="var(--icon-fg)" stroke-width="2"/></svg>
        <svg class="footer__icon" viewBox="0 0 42 42"><path d="M15 6 V16 Q15 20 21 20 Q27 20 27 16 V6 M19 6 V16 M23 6 V16 M21 20 V37" fill="none" stroke="var(--icon-fg)" stroke-width="2"/></svg>
        <svg class="footer__icon" viewBox="0 0 42 42"><path d="M22 5 Q14 14 18 24 L18 37 L23 37 L23 5 Z" fill="var(--icon-fg)"/></svg>
      </div>
    </footer>
  </section>

  <!-- Seite: Weißwein -->
  <section class="page page--right">
    <div class="brand"><span class="brand__square"></span>Pelkinger</div>

    <header class="section-head" style="left:128px; top:173px; width:326px;">
      <svg style="left:86px; top:-6px;" width="16" height="32" viewBox="0 0 16 32">
        <path d="M2 2 H14 Q15 16 8 18 Q1 16 2 2 Z" fill="var(--green)"/>
        <path d="M8 18 V29 M3 30 H13" stroke="var(--green)" stroke-width="1.8"/>
      </svg>
      <h2 class="section-head__title" style="left:104px;">Weisswein</h2>
    </header>

    <footer class="footer" style="left:187px;">
      <p class="footer__name">Heuriger Familie Pelkinger e.U.</p>
      <div class="footer__icons">
        <svg class="footer__icon" viewBox="0 0 42 42"><path d="M13 8 H29 Q30 22 21 24 Q12 22 13 8 Z M20 24 V34 M15 34 H27" fill="var(--icon-fg)" stroke="var(--icon-fg)" stroke-width="2"/></svg>
        <svg class="footer__icon" viewBox="0 0 42 42"><path d="M15 6 V16 Q15 20 21 20 Q27 20 27 16 V6 M19 6 V16 M23 6 V16 M21 20 V37" fill="none" stroke="var(--icon-fg)" stroke-width="2"/></svg>
        <svg class="footer__icon" viewBox="0 0 42 42"><path d="M22 5 Q14 14 18 24 L18 37 L23 37 L23 5 Z" fill="var(--icon-fg)"/></svg>
      </div>
    </footer>
  </section>

</main>
</body>
</html>
```